iVAK Company brochure For sales and Marketing

WE need a brochure design for our company called iVAK. The logo is gold. This is an Airline Maintenace Software Company. The software it is called iVAK.

We will like the Brochure to include our modules and a brief description on what they are about.

The front cover we want to have purple night sky screen. With our logo and out motto.

The first page can have the company bio. And the inside the Company modules description.

the back can have contact Sales information.

We will like this to be modern and with style. Ower mention Varnelle catalog.

please see out sample Web Site

http://tkrell42.sitebuild-demo.com/ivak

Target Market(s)

Airlines

Industry/Entity Type

Airline

Requirements
Must have
• gold, black , purple, grey and chrome. we like mature scenes or night sky
Nice to have

```html
<!DOCTYPE html>
<html lang="en">
<head>
<meta charset="utf-8">
<title>iVAK Modules Brochure Spread</title>
<link href="https://fonts.googleapis.com/css2?family=Titillium+Web:wght@300;400;700&display=swap" rel="stylesheet">
<style>
  :root{
    --bg:#cfcfcf;
    --purple-1:#8b63b2;
    --purple-2:#774aa6;
    --purple-3:#653897;
    --blue-1:#55ade0;
    --blue-2:#3a9fd9;
    --blue-3:#1f8ccd;
    --text:#ffffff;
    --shot-dark:#2a2a33;
    --shot-light:#e9edf3;
    --doc:#f7f7f7;
  }
  *{box-sizing:border-box;margin:0;padding:0}
  html,body{width:1200px;height:900px;overflow:hidden}
  body{background:var(--bg);font-family:"Titillium Web",sans-serif;color:var(--text);position:relative}
  .spread{position:absolute;left:80px;top:80px;width:1040px;height:740px;box-shadow:0 12px 30px rgba(0,0,0,.25)}
  .page{position:absolute;top:0;width:520px;height:740px;overflow:hidden}
  .page--left{left:0}
  .page--right{left:520px}
  .page-bands{position:absolute;inset:0}
  .module{position:absolute;display:flex;gap:18px;align-items:flex-start}
  .module-title{font-weight:700;font-size:13px;text-transform:uppercase;letter-spacing:.2px;margin-bottom:5px}
  .module-text{font-weight:300;font-size:10.5px;line-height:1.38;text-align:justify}
  .screen{flex:none;width:220px;height:140px;border-radius:2px;box-shadow:0 4px 10px rgba(0,0,0,.3);
    background:linear-gradient(90deg,var(--shot-dark) 0 14%,var(--shot-light) 14% 100%)}
  .screen--orders{background:linear-gradient(180deg,#2f4f9a 0 10%,transparent 10%),linear-gradient(90deg,var(--shot-dark) 0 14%,var(--shot-light) 14% 100%)}
  .screen--inventory{height:110px;background:linear-gradient(180deg,#3b6fc4 0 9%,transparent 9%),linear-gradient(90deg,var(--shot-dark) 0 12%,#f2f2f2 12% 100%)}
  .doc-page{flex:none;width:170px;height:200px;background:var(--doc);box-shadow:0 4px 10px rgba(0,0,0,.3)}
  .col{width:240px}
  .col--half{width:225px}
</style>
</head>
<body>
<main class="spread">
  <section class="page page--left">
    <svg class="page-bands" width="520" height="740" viewBox="0 0 520 740" aria-hidden="true">
      <rect width="520" height="740" fill="var(--purple-1)"/>
      <path d="M0 230 Q260 190 520 250 L520 740 L0 740Z" fill="var(--purple-2)"/>
      <path d="M0 485 Q260 445 520 505 L520 740 L0 740Z" fill="var(--purple-3)"/>
    </svg>

    <article class="module" style="left:24px;top:28px">
      <div class="screen" role="img" aria-label="Requisition module screen with pie charts and status panels"></div>
      <div class="col">
        <h2 class="module-title">The Requisition Module</h2>
        <p class="module-text">Real time creation of requisitions allows complete monitoring of all company part requirements. Requisitions automatically generate inventory transactions as defined by predefined reorder level requirements. Requisition information can be tied to orders and updates upon satisfaction of such requirements. The electronic quoting system provides a way to send and receive quotes via email or Spec2000 transactions.</p>
      </div>
    </article>

    <article class="module" style="left:24px;top:275px">
      <div class="screen screen--orders" role="img" aria-label="Orders module screen with order form and item list"></div>
      <div class="col">
        <h2 class="module-title">The Orders Modules</h2>
        <p class="module-text">The Orders module empowers you to create and monitor the following types of orders: Contract Order, Exchange In/Out Order, Loan Order, Purchase Order, Service Order, Repair Order, Customer Order, Rental Order, Manufacturer Order, Warranty Claim, Order Transfer, Receiving and Inspecting. Vendor performance can be graphically monitored. Electronic ordering via Spec2000 is available as standard. Various connections to industry purchasing portals are also supported.</p>
      </div>
    </article>

    <article class="module" style="left:24px;top:530px">
      <div class="screen screen--inventory" role="img" aria-label="Inventory module screen with colored planning bars"></div>
      <div class="col">
        <h2 class="module-title">The Inventory Module</h2>
        <p class="module-text">This functionality gives you the ability to control inventory within your organization from the basic part requirement through to warehousing, reservation and issuing of parts. Parts can be serialized, batched or kitted. Multiple locations can be optimized for minimum inventory levels. Packing and shipping provide detailed analysis of part movements, and give recommendations on surplus stock according to the operational requirements. Bar coding and RFID are supported for tracking of materials through your organization.</p>
      </div>
    </article>
  </section>

  <section class="page page--right">
    <svg class="page-bands" width="520" height="740" viewBox="0 0 520 740" aria-hidden="true">
      <rect width="520" height="740" fill="var(--blue-1)"/>
      <path d="M0 235 Q260 195 520 255 L520 740 L0 740Z" fill="var(--blue-2)"/>
      <path d="M0 490 Q260 450 520 510 L520 740 L0 740Z" fill="var(--blue-3)"/>
    </svg>

    <div class="module" style="left:24px;top:28px">
      <article class="col--half">
        <h2 class="module-title">The Financial Interface Module</h2>
        <p class="module-text">The Finance module provides an interface with the company financial software such as General Ledger, Accounts Payable and Receivable systems to feed them information. The financial information and accounting control over all financially related activity within the system. The fixed asset menu option provides valuation and depreciation data. Monthly balances, stock valuations and financial budgeting are all accessible within the system.</p>
      </article>
      <article class="col--half" style="margin-top:40px">
        <h2 class="module-title">The Link Module</h2>
        <p class="module-text">This subset of the Finance module allows the tracking and online approval of invoices received from vendors. It provides an efficient system-based communication between Accounts Payable and Purchasing for three-way match of invoices. Tolerance levels can be set to have the correct pricing. Electronic invoice data can be sent and received via Spec2000 or e-invoice formats.</p>
      </article>
    </div>

    <article class="module" style="left:30px;top:270px">
      <div class="doc-page" role="img" aria-label="Scanned maintenance document page with a technical drawing"></div>
      <div class="col" style="width:270px;margin-top:30px">
        <h2 class="module-title">The VakDoc Module</h2>
        <p class="module-text">VakDoc is a complete digital document management system used for the loading of manufacturer documentation (AMM, IPC, EMM, MPD and others). The system allows the automatic creation of data from these sources such as Maintenance Programs, Task Cards and Part Master Configurations. In addition to this any other hard copy documents, pictures and files can be stored. The module allows for security restrictions to various users or departments according to document type. VakDoc negates the need for separate maintenance document management systems, saving significant integration and support costs for the organization.</p>
      </div>
    </article>

    <article class="module" style="left:24px;top:525px">
      <div class="screen" role="img" aria-label="Engineering module screen with task list and details"></div>
      <div class="col">
        <h2 class="module-title">The Engineering Module</h2>
        <p class="module-text">The Engineering suite harnesses the power to manage maintenance requirements along with manufacturer and authority documents. Maintenance programs, ADs and SBs can be tracked and associated with task cards, which can be adjusted according to results. Electronic upload of data from manufacturers and scanning of logs saves time. Structural Sampling and control of component inspections are also included.</p>
      </div>
    </article>
  </section>
</main>
</body>
</html>
```